Innovative Freezer Label Design

Create a versatile and innovative freezer label design with universal appeal, suitable for different functionalities. The design should cater to a diverse audience, including those who freeze meals for meal prepping, batch cooking, and the restaurant industry. Our vision is a visually striking and distinctive design that embodies simplicity.

Example "our current labels feature essential details like "Contents" and "Date." We recognize these as crucial points of information. Currently, the challenge lies in creating various labels for different marketplaces, considering language barriers. A proposed solution involves the integration of universal icons to replace specific words, promoting practicality for international sales."

Kindly note that design concepts should not be restricted to our current product, brand guideline, logo, or the provided example.

Our goal is not only product differentiation but also increased sales through a blend of functionality and aesthetics.

The following are examples of freezer labels designs. Kindly do not restrict your designs to the examples. The designs must be universal (for language barrier purposes)

Examples:
https://www.tackvora.co.uk/pin/5827164039281736401/
https://www.tackvora.co.uk/pin/5827164039281736405/
https://www.tackvora.co.uk/pin/5827164039281736394/
https://www.tackvora.co.uk/pin/5827164039281736308/
https://www.tackvora.co.uk/pin/5827164039281797750/

Please reach out if you have any questions.

Thank you

```html
<!DOCTYPE html>
<html lang="en">
<head>
<meta charset="utf-8">
<title>Freezer Label Designs</title>
<link href="https://fonts.googleapis.com/css2?family=Roboto:wght@300&display=swap" rel="stylesheet">
<style>
  :root {
    --backdrop: #f2ca92;
    --label-paper: #fcf9f4;
    --label-edge: #ffffff;
    --brand-red: #e8323a;
    --ink: #1e1e1e;
    --rule: #6e6b68;
    --veg-orange: #f39a2b;
    --fruit-red: #d0242d;
    --roast-brown: #8c4a22;
    --steak-red: #b8414a;
    --fish-orange: #f7a531;
    --cake-red: #d85a4c;
  }
  * { margin: 0; padding: 0; box-sizing: border-box; }
  html, body {
    width: 1000px; height: 1200px; overflow: hidden;
    background: var(--backdrop);
  }
  .sheet { position: relative; width: 1000px; height: 1200px; }

  .freezer-label {
    position: absolute;
    width: 754px; height: 382px;
    background: var(--label-edge);
    box-shadow: 0 3px 4px rgba(120, 80, 30, 0.25);
  }
  .freezer-label--square { left: 122px; top: 152px; }
  .freezer-label--rounded { left: 124px; top: 668px; border-radius: 24px; }

  .label-frame {
    position: absolute; inset: 4px;
    background: var(--label-paper);
    border: 5px solid var(--brand-red);
    overflow: hidden;
  }
  .freezer-label--rounded .label-frame { border-radius: 20px; }

  .food-icon {
    position: absolute; top: 36px;
    width: 70px; height: 62px;
    border-radius: 18px;
  }
  .food-icon--veg    { left: 29px;  background: linear-gradient(135deg, var(--veg-orange), var(--fruit-red)); }
  .food-icon--fruit  { left: 149px; background: linear-gradient(90deg, var(--fruit-red), #9cc93c); }
  .food-icon--poultry{ left: 271px; background: var(--roast-brown); }
  .food-icon--meat   { left: 396px; background: var(--steak-red); border-radius: 30px; }
  .food-icon--fish   { left: 519px; background: var(--fish-orange); border-radius: 30px; }
  .food-icon--dessert{ left: 641px; width: 50px; background: linear-gradient(180deg, var(--cake-red), #8c4a2e); }

  .field-icon { position: absolute; }
  .field-icon--contents { left: 74px; top: 152px; width: 66px; height: 64px; }
  .field-icon--date { left: 82px; top: 284px; width: 66px; height: 56px; }

  .write-rule {
    position: absolute; left: 69px; top: 247px;
    width: 600px; height: 2px; background: var(--rule);
  }

  .date-slash {
    position: absolute; top: 284px;
    font-family: "Roboto", sans-serif; font-weight: 300;
    font-size: 50px; line-height: 1; color: var(--ink);
  }
  .date-slash--day { left: 296px; }
  .date-slash--month { left: 454px; }

  .brand-mark {
    position: absolute; right: 18px; bottom: 14px;
    display: flex; align-items: center; gap: 7px;
  }
  .brand-dot {
    width: 10px; height: 10px; border-radius: 50%;
    background: var(--brand-red);
  }
  .brand-name {
    font-family: "Roboto", sans-serif; font-weight: 300;
    font-size: 20px; line-height: 1; color: var(--brand-red);
  }
</style>
</head>
<body>
<main class="sheet">

  <section class="freezer-label freezer-label--square">
    <div class="label-frame">
      <div class="food-icon food-icon--veg" role="img" aria-label="Vegetables icon: carrot and tomato"></div>
      <div class="food-icon food-icon--fruit" role="img" aria-label="Fruit icon: apple and pear"></div>
      <div class="food-icon food-icon--poultry" role="img" aria-label="Poultry icon: roast chicken"></div>
      <div class="food-icon food-icon--meat" role="img" aria-label="Meat icon: steak"></div>
      <div class="food-icon food-icon--fish" role="img" aria-label="Fish icon"></div>
      <div class="food-icon food-icon--dessert" role="img" aria-label="Dessert icon: cupcake"></div>

      <svg class="field-icon field-icon--contents" viewBox="0 0 66 64" role="img" aria-label="Contents">
        <rect x="18" y="6" width="42" height="54" rx="5" fill="none" stroke="#1e1e1e" stroke-width="3.5"/>
        <path d="M24 2v8M30 2v8M36 2v8M42 2v8M48 2v8M54 2v8" stroke="#1e1e1e" stroke-width="2"/>
        <path d="M30 20h22M30 28h22M34 36h18M36 44h16" stroke="#1e1e1e" stroke-width="2"/>
        <path d="M4 14l22 24-3 6-6-3L-1 18z" fill="#1e1e1e" transform="translate(3 0)"/>
      </svg>

      <div class="write-rule"></div>

      <svg class="field-icon field-icon--date" viewBox="0 0 66 56" role="img" aria-label="Date">
        <rect x="2" y="8" width="54" height="38" rx="4" fill="none" stroke="#1e1e1e" stroke-width="3.5"/>
        <rect x="2" y="8" width="54" height="9" fill="#1e1e1e"/>
        <path d="M14 3v10M44 3v10" stroke="#1e1e1e" stroke-width="3.5"/>
        <g fill="#1e1e1e">
          <rect x="8" y="22" width="7" height="6"/><rect x="19" y="22" width="7" height="6"/><rect x="30" y="22" width="7" height="6"/><rect x="41" y="22" width="7" height="6"/>
          <rect x="8" y="32" width="7" height="6"/><rect x="19" y="32" width="7" height="6"/><rect x="30" y="32" width="7" height="6"/>
        </g>
        <circle cx="52" cy="42" r="11" fill="#fcf9f4" stroke="#1e1e1e" stroke-width="3"/>
        <path d="M52 36v7h5" fill="none" stroke="#1e1e1e" stroke-width="2.5"/>
      </svg>

      <span class="date-slash date-slash--day">/</span>
      <span class="date-slash date-slash--month">/</span>

      <div class="brand-mark"><span class="brand-dot"></span><span class="brand-name">Frostly</span></div>
    </div>
  </section>

  <section class="freezer-label freezer-label--rounded">
    <div class="label-frame">
      <div class="food-icon food-icon--veg" role="img" aria-label="Vegetables icon: carrot and tomato"></div>
      <div class="food-icon food-icon--fruit" role="img" aria-label="Fruit icon: apple and pear"></div>
      <div class="food-icon food-icon--poultry" role="img" aria-label="Poultry icon: roast chicken"></div>
      <div class="food-icon food-icon--meat" role="img" aria-label="Meat icon: steak"></div>
      <div class="food-icon food-icon--fish" role="img" aria-label="Fish icon"></div>
      <div class="food-icon food-icon--dessert" role="img" aria-label="Dessert icon: cupcake"></div>

      <svg class="field-icon field-icon--contents" viewBox="0 0 66 64" role="img" aria-label="Contents">
        <rect x="18" y="6" width="42" height="54" rx="5" fill="none" stroke="#1e1e1e" stroke-width="3.5"/>
        <path d="M24 2v8M30 2v8M36 2v8M42 2v8M48 2v8M54 2v8" stroke="#1e1e1e" stroke-width="2"/>
        <path d="M30 20h22M30 28h22M34 36h18M36 44h16" stroke="#1e1e1e" stroke-width="2"/>
        <path d="M4 14l22 24-3 6-6-3L-1 18z" fill="#1e1e1e" transform="translate(3 0)"/>
      </svg>

      <div class="write-rule"></div>

      <svg class="field-icon field-icon--date" viewBox="0 0 66 56" role="img" aria-label="Date">
        <rect x="2" y="8" width="54" height="38" rx="4" fill="none" stroke="#1e1e1e" stroke-width="3.5"/>
        <rect x="2" y="8" width="54" height="9" fill="#1e1e1e"/>
        <path d="M14 3v10M44 3v10" stroke="#1e1e1e" stroke-width="3.5"/>
        <g fill="#1e1e1e">
          <rect x="8" y="22" width="7" height="6"/><rect x="19" y="22" width="7" height="6"/><rect x="30" y="22" width="7" height="6"/><rect x="41" y="22" width="7" height="6"/>
          <rect x="8" y="32" width="7" height="6"/><rect x="19" y="32" width="7" height="6"/><rect x="30" y="32" width="7" height="6"/>
        </g>
        <circle cx="52" cy="42" r="11" fill="#fcf9f4" stroke="#1e1e1e" stroke-width="3"/>
        <path d="M52 36v7h5" fill="none" stroke="#1e1e1e" stroke-width="2.5"/>
      </svg>

      <span class="date-slash date-slash--day">/</span>
      <span class="date-slash date-slash--month">/</span>

      <div class="brand-mark"><span class="brand-dot"></span><span class="brand-name">Frostly</span></div>
    </div>
  </section>

</main>
</body>
</html>
```